Flyer-Design für Kindertagesstätte
Helmsteds Kinderhafen suchte ein neues Design in der Kategorie Flyer und hat ein Projekt auf grafikfinden.de gestartet.
Zielgruppe
Wir sind eine Kindertagesstätte und wollen eine Baby-Kind-Spielgruppe jeden Mittwoch in unserer Kita von 09.00 Uhr bis 11.00 Uhr anbieten.
Aufgabenstellung
Unser LOGO muss im Flyer enthalten sein, auf jeden Fall ein Bild wenn möglich mit mehreren Babys/Kleinkindern bis 1,5 Jahre. Wir benötigen den Flyer in DIN lang - bunt - 1 seitig.
Folgender Text sollte enthalten: Baby-Kind-Spielgruppe, jeden mittwoch in unserer Kita 'Helmsteds Kinderhafen' von 09.00 Uhr bis 11.00 Uhr. Die Spielgruppe wird durch unser ausgebildetes Fachpersonal begleitet.

```html
<!DOCTYPE html>
<html lang="de">
<head>
<meta charset="utf-8">
<title>Baby-Krabbel-Spielgruppe – Helmsteds Kinderhafen</title>
<link rel="stylesheet" href="https://fonts.googleapis.com/css2?family=Bree+Serif&family=Open+Sans:wght@400;600;700&display=swap">
<style>
  :root {
    --orange: #e8661c;
    --green: #9ac31c;
    --white: #ffffff;
    --ink: #2b2b2b;
    --page: #ffffff;
    --pink: #e0217a;
    --blue: #2a8fd6;
    --yellow: #f5c518;
    --brown: #5a2a1e;
  }
  html, body {
    margin: 0;
    width: 1129px;
    height: 1200px;
    overflow: hidden;
    background: var(--page);
  }
  .canvas {
    position: relative;
    width: 1129px;
    height: 1200px;
  }
  .flyer {
    position: absolute;
    left: 0;
    top: 335px;
    width: 1129px;
    height: 529px;
    display: block;
  }
  .fill-orange { fill: var(--orange); }
  .fill-green { fill: var(--green); }
  .fill-white { fill: var(--white); }
  .fill-pink { fill: var(--pink); }
  .fill-blue { fill: var(--blue); }
  .fill-yellow { fill: var(--yellow); }
  .headline {
    font-family: "Bree Serif", Georgia, serif;
    font-size: 26px;
    fill: var(--orange);
  }
  .subline {
    font-family: "Open Sans", Arial, sans-serif;
    font-weight: 600;
    font-size: 16px;
    fill: var(--ink);
  }
  .section-title {
    font-family: "Open Sans", Arial, sans-serif;
    font-weight: 600;
    font-size: 18.5px;
    fill: var(--white);
  }
  .body-copy {
    font-family: "Open Sans", Arial, sans-serif;
    font-size: 11.3px;
    fill: var(--white);
  }
  .body-copy .strong { font-weight: 700; }
  .badge-day {
    font-family: "Open Sans", Arial, sans-serif;
    font-weight: 600;
    font-size: 25px;
    fill: var(--white);
  }
  .badge-time {
    font-family: "Open Sans", Arial, sans-serif;
    font-size: 14px;
    fill: var(--white);
  }
  .contact {
    font-family: "Open Sans", Arial, sans-serif;
    font-size: 14.5px;
    letter-spacing: 1px;
    fill: var(--white);
  }
  .brand-name {
    font-family: "Open Sans", Arial, sans-serif;
    font-weight: 700;
    font-size: 17px;
    fill: var(--brown);
  }
</style>
</head>
<body>
<main class="canvas">
  <svg class="flyer" viewBox="0 0 992 465" xmlns="http://www.w3.org/2000/svg">
    <defs>
      <linearGradient id="photo-tones" x1="0" y1="0" x2="1" y2="1">
        <stop offset="0" stop-color="#efe6df"/>
        <stop offset="0.5" stop-color="#e9d2c6"/>
        <stop offset="1" stop-color="#c9b8ae"/>
      </linearGradient>
      <linearGradient id="toy-tones" x1="0" y1="0" x2="1" y2="1">
        <stop offset="0" stop-color="#f2c230"/>
        <stop offset="0.5" stop-color="#e0506b"/>
        <stop offset="1" stop-color="#2d6fc4"/>
      </linearGradient>
    </defs>

    <!-- background -->
    <rect class="fill-white" width="992" height="465"/>

    <!-- orange wave band -->
    <path class="fill-orange" d="M300,152 C430,138 560,200 700,220 C820,238 920,242 992,245 V465 H0 V380 Z"/>

    <!-- photo area with curved edge -->
    <g class="photo" role="img" aria-label="Foto: Baby krabbelt mit buntem Spielzeug auf dem Boden">
      <path d="M0,0 H348 C372,150 330,330 205,400 C135,438 55,444 0,428 Z" fill="url(#photo-tones)" stroke="#ffffff" stroke-width="9"/>
    </g>

    <!-- confetti dots -->
    <circle class="fill-yellow" cx="658" cy="59" r="4"/>
    <circle class="fill-pink" cx="617" cy="214" r="12"/>
    <circle class="fill-green" cx="366" cy="206" r="17"/>
    <circle class="fill-blue" cx="980" cy="144" r="8"/>
    <circle class="fill-pink" cx="349" cy="349" r="8"/>
    <circle class="fill-yellow" cx="287" cy="379" r="4"/>
    <circle class="fill-blue" cx="791" cy="295" r="8"/>
    <circle class="fill-yellow" cx="695" cy="178" r="4"/>
    <circle class="fill-green" cx="532" cy="180" r="3"/>
    <circle class="fill-pink" cx="951" cy="86" r="4"/>

    <!-- day badge -->
    <g class="day-badge" transform="rotate(-14 258 296)">
      <ellipse class="fill-green" cx="258" cy="296" rx="94" ry="62"/>
      <ellipse cx="258" cy="296" rx="84" ry="53" fill="none" stroke="#ffffff" stroke-width="2" stroke-dasharray="9 5"/>
      <text class="badge-day" x="258" y="292" text-anchor="middle">Mittwochs</text>
      <text class="badge-time" x="258" y="313" text-anchor="middle">09.00 bis 11.00 Uhr</text>
    </g>

    <!-- headline -->
    <text class="headline" x="385" y="105">Baby-Krabbel-Spielgruppe</text>
    <text class="subline" x="386" y="132">Für Kinder von 6 bis 18 Monaten</text>

    <!-- brand -->
    <g class="brand">
      <circle class="fill-orange" cx="877" cy="90" r="30"/>
      <text class="brand-name" x="877" y="160" text-anchor="middle">
        <tspan x="877">Helmsteds</tspan>
        <tspan x="877" dy="21">Kinderhafen</tspan>
      </text>
    </g>

    <!-- body text -->
    <text class="section-title" x="387" y="267">Jeden Mittwoch in unserer Kita</text>
    <text class="body-copy" x="387" y="290">
      <tspan x="387">Die Spielgruppe wird durch unser ausgebildetes</tspan>
      <tspan x="387" dy="15">Fachpersonal begleitet.</tspan>
      <tspan x="387" dy="30">Voranmeldungen bitte unter telefonisch unter: <tspan class="strong">0351-4820716</tspan></tspan>
      <tspan x="387" dy="15">oder unter <tspan class="strong">www.helmsteds-kinderhafen.de.</tspan> Spielgruppe ist</tspan>
      <tspan x="387" dy="15">öffentlich und kostenfrei.</tspan>
    </text>

    <!-- illustration area -->
    <g class="toys-illustration" role="img" aria-label="Illustration: Spielzeug mit Dinosaurier, Rakete und Ball">
      <path d="M780,270 C840,250 930,255 992,262 V465 H760 C770,400 760,320 780,270 Z" fill="url(#toy-tones)" opacity="0.85"/>
    </g>

    <!-- contact footer -->
    <g class="contact-web">
      <circle cx="284" cy="427" r="10" fill="none" stroke="#ffffff" stroke-width="2"/>
      <ellipse cx="284" cy="427" rx="4.5" ry="10" fill="none" stroke="#ffffff" stroke-width="1.5"/>
      <line x1="274" y1="427" x2="294" y2="427" stroke="#ffffff" stroke-width="1.5"/>
      <line x1="276" y1="421" x2="292" y2="421" stroke="#ffffff" stroke-width="1.2"/>
      <line x1="276" y1="433" x2="292" y2="433" stroke="#ffffff" stroke-width="1.2"/>
      <text class="contact" x="305" y="432">www.helmsteds-kinderhafen.de</text>
    </g>
    <g class="contact-phone">
      <circle class="fill-white" cx="605" cy="427" r="10"/>
      <path class="fill-orange" d="M601,421 c1,-1 2,-1 2.5,0 l1.5,2.5 c0.4,0.8 0,1.5 -0.8,2 c0.8,1.8 2,3 3.8,3.8 c0.5,-0.8 1.2,-1.2 2,-0.8 l2.5,1.5 c1,0.5 1,1.5 0,2.5 c-1.5,1.5 -4,1.5 -7,-1 c-3,-2.5 -5,-5.5 -5,-7.5 c0,-1.2 0.3,-2.2 0.5,-3 Z"/>
      <text class="contact" x="622" y="432">0351-4820716</text>
    </g>
  </svg>
</main>
</body>
</html>
```